Golden Years Wellness Roadmap: This is my second book. The first was Eldercare Compass

I need a book cover design for: GOLDEN YEARS WELLNESS ROADMAP: A NO-EXPENSE METHOD FOR FINISHING YOUR LATER-LIFE MOSAIC WITH POOLED KVB CARE SCHEMES by Derek Holloway Neil Osgrove & Martin Quarles. This book is designed for business owners, CEO's, CFO's and Human Resources. The cover needs to be professional and focused on business. The purpose of this book is to educate business owners and their management about a zero cost retiree health plan. This is a first of it's kind solution that every business needs to learn about.

Target Market(s)

Business owners, CEO's, CFO's and Human Resources

Requirements
Nice to have
• I want the design to be clean and professional since it is focused on business executives

```html
<!DOCTYPE html>
<html lang="en">
<head>
<meta charset="utf-8">
<title>Golden Years Wellness Roadmap – Book Cover</title>
<link rel="stylesheet" href="https://fonts.googleapis.com/css2?family=Jost:wght@500;600&display=swap">
<style>
  :root {
    --stage: #ececec;
    --cover-white: #ffffff;
    --brand-blue: #1d4eaa;
    --deep-navy: #1f2766;
    --photo-light: #e4edf7;
    --photo-pale: #cddcee;
    --photo-mid: #9dbadf;
    --photo-steel: #6f95cc;
    --photo-deep: rgba(32, 82, 172, 0.55);
  }
  * { margin: 0; padding: 0; box-sizing: border-box; }
  html, body {
    width: 1200px;
    height: 663px;
    overflow: hidden;
    background: var(--stage);
  }
  .stage {
    width: 1200px;
    height: 663px;
    display: flex;
    align-items: center;
    justify-content: center;
  }
  .book-cover {
    width: 410px;
    height: 600px;
    background: var(--cover-white);
    display: flex;
    flex-direction: column;
    font-family: "Jost", "Futura", sans-serif;
    box-shadow: 0 6px 22px rgba(0,0,0,0.18);
  }
  .cover-photo {
    height: 251px;
    flex: none;
    background:
      radial-gradient(circle at 30% 50%, var(--photo-deep) 0%, rgba(32, 82, 172, 0) 42%),
      radial-gradient(circle at 68% 62%, rgba(255,255,255,0.55) 0%, rgba(255,255,255,0) 30%),
      linear-gradient(105deg, var(--photo-light) 0%, var(--photo-pale) 35%, var(--photo-mid) 72%, var(--photo-steel) 100%);
  }
  .accent-band {
    height: 13px;
    flex: none;
    background: var(--brand-blue);
  }
  .title-block {
    flex: 1;
    display: flex;
    flex-direction: column;
    align-items: center;
    justify-content: center;
    text-align: center;
    padding: 0 24px;
  }
  .title {
    font-weight: 500;
    line-height: 1;
    text-transform: uppercase;
  }
  .title-line { display: block; }
  .title-line--first {
    color: var(--brand-blue);
    font-size: 40px;
    letter-spacing: 3px;
  }
  .title-line--main {
    color: var(--brand-blue);
    font-size: 58px;
    letter-spacing: 2px;
    margin-top: 4px;
  }
  .title-line--last {
    color: var(--deep-navy);
    font-size: 46px;
    letter-spacing: 6px;
    margin-top: 6px;
  }
  .subtitle {
    margin-top: 20px;
    font-weight: 600;
    font-size: 13px;
    line-height: 1.4;
    letter-spacing: 1.6px;
    text-transform: uppercase;
    color: var(--deep-navy);
  }
  .subtitle-lead { color: var(--brand-blue); display: block; }
  .subtitle-line { display: block; }
  .author-band {
    height: 68px;
    flex: none;
    background: var(--brand-blue);
    display: flex;
    align-items: center;
    justify-content: center;
  }
  .authors {
    color: var(--cover-white);
    font-weight: 600;
    font-size: 12px;
    letter-spacing: 1.2px;
    text-transform: uppercase;
  }
</style>
</head>
<body>
  <main class="stage">
    <article class="book-cover">
      <div class="cover-photo" role="img" aria-label="Photo of a white jigsaw puzzle with a missing blue cross-shaped section beside a stethoscope, in soft blue tones"></div>
      <div class="accent-band"></div>
      <section class="title-block">
        <h1 class="title">
          <span class="title-line title-line--first">Golden Years</span>
          <span class="title-line title-line--main">Wellness</span>
          <span class="title-line title-line--last">Roadmap</span>
        </h1>
        <p class="subtitle">
          <span class="subtitle-lead">A No-Expense Method for</span>
          <span class="subtitle-line">Finishing Your Later-Life Mosaic</span>
          <span class="subtitle-line">With Pooled KVB Care Schemes</span>
        </p>
      </section>
      <footer class="author-band">
        <p class="authors">Derek Holloway, Neil Osgrove &amp; Martin Quarles</p>
      </footer>
    </article>
  </main>
</body>
</html>
```